Education related business need name card design

We need name card design for long term study agent.
Company name is Harbor Lantern.
We support clients to connect to the world.
Clients are Japanese family who has primary and secondary school students.

Company Logo is reflection of the globe and HL (Harbor Lantern).
Since business is related to education, we would like to show reliability and love to see the world map (atlas) in the name card.

Target Market(s)

late 30's to 50's parents of primary and secondary students who are enthusiastic for education. Secondary school management

Industry/Entity Type

Education

Contact Information for Business Card

Company name, Address, Official position, Name, Phone number, Mobile number, email address,

Font styles to use
Serif
Other font styles liked:
• Century Gothic(logo)

Requirements
Must have
• Since businee is related to education, we would like to show reliability and love to see the world map (atlas) in the name card.

```html
<!DOCTYPE html>
<html lang="en">
<head>
<meta charset="utf-8">
<title>Harbor Lantern – Business Card</title>
<link rel="stylesheet" href="https://fonts.googleapis.com/css2?family=Lato:wght@400;700&display=swap">
<style>
  :root {
    --stage: #e9ebef;
    --card: #ffffff;
    --navy: #1f3a93;
    --royal: #2456b0;
    --sky: #3d8fdc;
    --ink: #1d1d22;
    --map-grey: #d6d8de;
    --map-grey-soft: #e9ebef;
  }
  * { box-sizing: border-box; margin: 0; padding: 0; }
  html, body {
    width: 1200px; height: 800px; overflow: hidden;
    background: var(--stage);
    font-family: "Lato", Arial, sans-serif;
  }
  .stage {
    position: relative; width: 1200px; height: 800px;
    display: flex; align-items: center; justify-content: center; gap: 50px;
  }
  .card {
    position: relative; width: 525px; height: 300px;
    background: var(--card); border-radius: 14px; overflow: hidden;
    box-shadow: 0 6px 22px rgba(20, 30, 60, 0.18);
  }

  /* Front */
  .front-map {
    position: absolute; left: 18px; top: 16px; right: 14px; bottom: 22px;
    border-radius: 70px 30px 110px 60px;
    background: linear-gradient(160deg, var(--navy) 0%, var(--royal) 45%, var(--sky) 100%);
    opacity: 0.92;
  }
  .front-brand {
    position: absolute; left: 110px; top: 118px;
    display: flex; align-items: center; gap: 14px;
  }
  .brand-dot {
    width: 58px; height: 58px; border-radius: 50%;
    background: var(--card);
  }
  .front-brand .brand-name {
    color: var(--card); font-size: 28px; font-weight: 400; line-height: 1.05;
  }

  /* Back */
  .back-brand {
    position: absolute; right: 30px; top: 28px;
    display: flex; align-items: center; gap: 12px;
  }
  .back-brand .brand-dot { width: 46px; height: 46px; background: var(--royal); }
  .back-brand .brand-name {
    color: var(--royal); font-size: 21px; font-weight: 400; line-height: 1.05;
  }
  .address {
    position: absolute; right: 30px; top: 86px; text-align: right;
    color: var(--ink); font-size: 13px; line-height: 1.35;
  }
  .back-map {
    position: absolute; left: 70px; right: 10px; top: 150px; bottom: 10px;
    border-radius: 60px 40px 80px 50px;
    background: radial-gradient(ellipse at 55% 50%, var(--map-grey) 0%, var(--map-grey-soft) 60%, rgba(233,235,239,0) 100%);
  }
  .swoosh { position: absolute; left: 0; top: 0; width: 525px; height: 300px; }
  .holder {
    position: absolute; left: 32px; top: 184px; color: var(--ink);
  }
  .holder-name { color: var(--royal); font-size: 19px; font-weight: 700; line-height: 22px; }
  .holder-title { font-size: 12px; line-height: 15px; }
  .contacts { list-style: none; margin-top: 8px; }
  .contacts li {
    display: flex; align-items: center; gap: 9px;
    font-size: 14px; line-height: 19px;
  }
  .contacts svg { width: 14px; height: 14px; flex: none; }
</style>
</head>
<body>
<main class="stage">

  <section class="card card-front">
    <div class="front-map" role="img" aria-label="World map in blue tones covering the card"></div>
    <div class="front-brand">
      <span class="brand-dot"></span>
      <span class="brand-name">Harbor Lantern<br>Pte.Ltd.</span>
    </div>
  </section>

  <section class="card card-back">
    <div class="back-map" role="img" aria-label="Faint grey world map behind the contact details"></div>
    <svg class="swoosh" viewBox="0 0 525 300" aria-hidden="true">
      <path d="M0,148 C170,110 360,104 525,138 L525,141 C360,112 170,122 0,160 Z" fill="var(--sky)"/>
      <path d="M0,160 C170,122 360,112 525,141 L525,145 C360,122 170,140 0,178 Z" fill="var(--navy)"/>
    </svg>

    <div class="back-brand">
      <span class="brand-dot"></span>
      <span class="brand-name">Harbor Lantern<br>Pte.Ltd.</span>
    </div>
    <p class="address">48 Beacon Row 12th Street<br>Calder, TX 78701</p>

    <div class="holder">
      <h1 class="holder-name">Mara Ellison</h1>
      <p class="holder-title">Owner &amp; CEO</p>
      <ul class="contacts">
        <li>
          <svg viewBox="0 0 16 16" aria-hidden="true"><path fill="var(--royal)" d="M3 2h3l1.5 3.5-2 1.2a8 8 0 0 0 3.8 3.8l1.2-2L14 10v3a1.5 1.5 0 0 1-1.5 1.5A11.5 11.5 0 0 1 1.5 3.5 1.5 1.5 0 0 1 3 2z"/></svg>
          512-555-01846
        </li>
        <li>
          <svg viewBox="0 0 16 16" aria-hidden="true"><rect x="1" y="3" width="14" height="10" rx="1" fill="var(--royal)"/><path d="M1.5 3.5 8 9l6.5-5.5" fill="none" stroke="#fff" stroke-width="1.2"/></svg>
          mara@harborlantern.com
        </li>
        <li>
          <svg viewBox="0 0 16 16" aria-hidden="true"><circle cx="8" cy="8" r="7" fill="var(--royal)"/><g fill="none" stroke="#fff" stroke-width="1"><ellipse cx="8" cy="8" rx="3" ry="7"/><path d="M1 8h14M2.5 4.5h11M2.5 11.5h11"/></g></svg>
          www.harborlantern.com
        </li>
      </ul>
    </div>
  </section>

</main>
</body>
</html>
```